Social Movement/Church Plant Website - KindAshbury.com

We need a website for our church plant startup, however we want the focus of the landing page to be around #kindashbury - that we are an organization that is FOR our town (Loveland). The site will include serving project events, social events, a place to sign up for emails, a blog, a place to give, etc. All the elements we know we want are currently at kindashbury.com . Please check this for copy.

We want this to be easy to edit as a non-developer.

I have included several logos with our colors, as well as an ai file to give you an idea of how we want the design to look and feel - also includes our branded fonts

Target Market(s)

People who live in the Northern CO area

Font styles to use
Serif
Sans Serif

Requirements
Must have
• Events (serve and social), Blog section, A place to get involved - where to give and to sign up for emails. Must match our branding colors and style hex 4c7991.
Should not have
• Should not be focused on the actual church plant on the home page. There can be some back end stuff about it, but the focus should be #kindashbury.

```html
<!DOCTYPE html>
<html lang="en">
<head>
<meta charset="utf-8">
<title>KindAshbury.com — For Our Town</title>
<link href="https://fonts.googleapis.com/css2?family=Roboto+Condensed:wght@400;700&family=Open+Sans:wght@400;600&family=Roboto+Slab:wght@400;700&display=swap" rel="stylesheet">
<style>
:root{
  --brand:#4c7991;
  --navy:#41667b;
  --navy-deep:#2f4b5c;
  --navy-band:#4c7991;
  --slate:#5c6f86;
  --red:#c23b4d;
  --red-dark:#a8303f;
  --outer:#dbe3eb;
  --white:#ffffff;
  --ink:#3a3f4a;
  --muted:#8a93a3;
  --line:#e3e7ed;
  --panel:#f4f6f9;
  --head:"Roboto Condensed", "Arial Narrow", sans-serif;
  --body:"Open Sans", Arial, sans-serif;
  --serif:"Roboto Slab", Georgia, serif;
}
*{box-sizing:border-box;margin:0;padding:0}
html,body{width:1200px;height:5012px;overflow:hidden}
body{
  background:linear-gradient(to bottom,var(--navy) 0,var(--navy) 580px,var(--outer) 580px);
  font-family:var(--body);color:var(--ink);font-size:12px;line-height:1.5;
}
.topbar{height:32px;background:var(--navy-deep);display:flex;align-items:center;justify-content:space-between;padding:0 24px;color:#c3d0da;font-size:10px}
.topbar .donate{background:var(--red);color:#fff;font-family:var(--head);font-weight:700;padding:4px 14px;font-size:10px;letter-spacing:.5px}
.page{width:880px;margin:0 auto;background:var(--white)}
section{position:relative;overflow:hidden}
.site-header{position:relative;height:96px;display:flex;align-items:center;justify-content:space-between;padding:0 20px}
.brand{display:flex;align-items:center;gap:12px}
.brand-mark{width:52px;height:52px;background:var(--brand)}
.brand-name{font-family:var(--head);font-weight:700;font-size:18px;color:var(--brand)}
.contact{display:flex;gap:22px;font-size:10px;color:var(--muted);position:absolute;left:92px;top:8px}
.search{width:32px;height:32px;border:1px solid var(--line);display:grid;place-items:center}
.main-nav{height:24px;background:var(--red);display:flex;align-items:center;padding:0 14px;gap:26px;font-family:var(--head);font-weight:700;font-size:10px;color:#fff;letter-spacing:.5px}
.main-nav .active{background:var(--red-dark);padding:5px 10px}
.hero{height:428px;background:linear-gradient(160deg,#e7c24a 0%,#3f6a9a 38%,#6b8296 70%,#2e4250 100%)}
.hero .dots{position:absolute;bottom:16px;left:50%;transform:translateX(-50%);display:flex;gap:8px}
.dots i{width:8px;height:8px;border-radius:50%;background:rgba(255,255,255,.5);display:block}
.dots i.on{background:#fff}
.photo{display:block}
.features{height:348px;padding:20px 28px 0}
.cards4{display:grid;grid-template-columns:repeat(4,184px);gap:28px;justify-content:space-between}
.feature{height:200px;background:var(--navy)}
.feature.red{background:var(--red)}
.feature .top{height:64px;display:flex;flex-direction:column;align-items:center;justify-content:center;gap:6px;color:#fff;font-family:var(--head);font-weight:700;font-size:12px;letter-spacing:1px}
.feature .photo{height:136px;margin:0 10px;background:linear-gradient(135deg,#8c9ca8,#4a5e6a)}
.activism{display:flex;align-items:center;margin-top:30px;gap:40px}
.activism h2{font-family:var(--serif);font-size:28px;color:var(--brand);font-weight:700;line-height:1}
.activism h2 small{display:block;font-family:var(--body);font-size:9px;color:var(--red);font-weight:400;margin-top:4px}
.activism p{width:380px;font-size:10px;color:var(--muted);margin-left:80px}
.btn{display:inline-flex;align-items:center;gap:8px;background:var(--red);color:#fff;font-family:var(--head);font-weight:700;font-size:10px;padding:8px 14px;letter-spacing:.5px;white-space:nowrap}
.btn .sq{width:12px;height:12px;background:#fff;opacity:.85}
.section-title{font-family:var(--head);font-weight:700;font-size:17px;letter-spacing:1px;text-align:center;text-transform:uppercase}
.rights{height:584px;background:var(--navy-band);padding:36px 28px 0;color:#fff}
.collage{margin-top:36px;display:grid;grid-template-columns:196px 1fr 196px;grid-template-rows:236px 236px;gap:12px}
.collage .big{grid-row:1/3;grid-column:2;background:linear-gradient(180deg,#5b7f9a,#2a4050 70%,#1d2c36)}
.collage .c1{background:linear-gradient(135deg,#c44a52,#7b4048)}
.collage .c2{background:linear-gradient(135deg,#7a9fb8,#3a5a72)}
.collage .c3{background:linear-gradient(135deg,#e2e4ea,#9aaeba)}
.collage .c4{background:linear-gradient(135deg,#b24050,#4b6b86)}
.events{height:488px;padding:66px 28px 0}
.events .section-title,.members .section-title,.news .section-title,.funds .section-title,.voices .section-title{color:var(--brand)}
.events-grid{display:grid;grid-template-columns:repeat(3,252px);justify-content:space-between;margin-top:40px}
.event .photo{height:170px}
.event h3{font-family:var(--head);font-size:13px;color:var(--brand);margin-top:14px}
.event .date{font-size:10px;color:var(--red)}
.event p{font-size:10px;color:var(--muted);margin-top:6px}
.event .more{font-size:10px;color:var(--brand);margin-top:8px}
.donation{height:320px;background:linear-gradient(135deg,#5f7489,#4d6177);padding:56px 28px 0;color:#fff}
.donation-row{display:flex;gap:30px;margin-top:34px}
.donate-form{width:290px;background:rgba(255,255,255,.12);padding:14px}
.field{height:30px;border-bottom:1px solid rgba(255,255,255,.35);font-size:10px;padding-top:8px;color:#e3e8ee}
.donation-text{width:360px;font-size:10px;color:#e0e6ec}
.btn-light{display:inline-block;margin-top:16px;background:#fff;color:var(--slate);font-family:var(--head);font-weight:700;font-size:10px;padding:7px 14px}
.voices{height:512px;padding:40px 28px 0}
.voices-panel{margin-top:28px;background:var(--panel);border:1px solid var(--line);padding:26px;display:grid;grid-template-columns:1fr 1fr;gap:40px 30px}
.quote{display:flex;gap:18px}
.quote .photo{width:100px;height:100px;flex:none}
.quote p{font-size:10px;color:var(--muted)}
.quote strong{display:block;margin-top:10px;font-family:var(--head);color:var(--brand);font-size:11px}
.quote span{font-size:9px;color:var(--red)}
.shop{height:328px;background:var(--red);padding:26px 28px 0;color:#fff}
.products{display:grid;grid-template-columns:repeat(4,184px);justify-content:space-between;margin-top:22px}
.product .photo{height:148px;background:linear-gradient(160deg,#d56473,#a93444)}
.product h3{font-family:var(--head);font-size:11px;margin-top:8px;line-height:1.3}
.product .cat{font-size:9px;opacity:.8;line-height:1.3}
.product .price{font-family:var(--head);font-weight:700;font-size:13px;margin-top:4px;line-height:1.3}
.product .actions{display:flex;gap:6px;margin-top:6px}
.product .actions span{border:1px solid rgba(255,255,255,.6);font-size:9px;padding:2px 8px;line-height:1.4}
.members{height:360px;padding:36px 28px 0}
.members-grid{display:grid;grid-template-columns:repeat(3,252px);justify-content:space-between;margin-top:34px}
.member .photo{height:170px}
.member h3{font-family:var(--head);font-size:12px;color:var(--brand);margin-top:12px}
.member .role{font-size:10px;color:var(--muted)}
.socials{display:flex;gap:6px;margin-top:10px}
.socials i{width:18px;height:18px;border-radius:50%;background:#c9d3dc;display:block}
.progress{height:320px;background:var(--navy-band);padding:40px 28px 0;color:#fff}
.progress-grid{display:grid;grid-template-columns:repeat(4,1fr);margin-top:70px;text-align:center}
.stat{display:flex;align-items:center;justify-content:center;gap:10px}
.stat b{font-family:var(--head);font-size:34px;color:var(--red);font-weight:400;line-height:1}
.stat .lbl{font-size:10px;color:#d3dee6;display:block;margin-top:4px}
.news{height:400px;padding:40px 28px 0}
.news-grid{display:grid;grid-template-columns:repeat(4,184px);justify-content:space-between;margin-top:30px}
.post .photo{height:150px}
.post h3{font-family:var(--head);font-size:12px;color:var(--brand);margin-top:12px}
.post .meta{font-size:9px;color:var(--muted);margin-top:4px}
.twitter{height:240px;background:linear-gradient(135deg,#c9485a,#b23646);padding:44px 90px 0;color:#fff;text-align:center}
.twitter .flag{position:absolute;left:0;top:0;width:100%;height:100%;background:radial-gradient(ellipse at 35% 60%,rgba(255,255,255,.10),rgba(255,255,255,0) 60%)}
.tw-mark{position:relative;width:26px;height:26px;border-radius:50%;background:#fff;margin:0 auto}
.twitter .handle{position:relative;font-size:10px;margin-top:6px}
.twitter p{font-size:11px;margin-top:14px;position:relative}
.twitter .dots{position:relative;justify-content:center;margin-top:16px;display:flex;gap:6px}
.funds{height:240px;padding:48px 28px 0}
.funds-grid{display:grid;grid-template-columns:repeat(4,1fr);margin-top:50px;text-align:center}
.fund .lbl{font-size:10px;color:var(--muted)}
.fund b{display:block;font-family:var(--head);font-size:28px;color:var(--brand);margin-top:6px}
.footer{height:292px;background:var(--navy);color:#fff;padding:44px 28px 0}
.footer-row{display:flex;align-items:center;gap:80px}
.footer-brand{font-family:var(--head);font-size:26px;font-weight:700;line-height:1.1;color:#fff;text-transform:uppercase}
.social-activity{display:flex;align-items:center;gap:8px;font-family:var(--head);font-size:15px}
.social-activity i{width:14px;height:14px;border-radius:50%;background:#fff;display:block}
.footer .circles{display:flex;gap:12px;justify-content:center;margin-top:60px}
.footer .circles i{width:30px;height:30px;border-radius:50%;border:2px solid rgba(255,255,255,.6);display:block}
.footer .rule{height:1px;background:rgba(255,255,255,.2);margin-top:40px}
.footer .legal{text-align:center;font-size:9px;color:#c3d0da;margin-top:14px}
</style>
</head>
<body>
<div class="topbar">
  <span>Welcome to KindAshbury.com — a movement for our town</span>
  <span class="donate">DONATE NOW</span>
</div>
<div class="page">
  <header class="site-header">
    <div class="brand"><div class="brand-mark"></div><span class="brand-name">KindAshbury</span></div>
    <div class="contact"><span>Ashbury, Northern Colorado</span><span>(970) 555-0142</span><span>hello@kindashbury.com</span></div>
    <div class="search"><svg width="14" height="14" viewBox="0 0 14 14"><circle cx="6" cy="6" r="4.5" fill="none" stroke="#4c7991" stroke-width="1.6"/><line x1="9.3" y1="9.3" x2="13" y2="13" stroke="#4c7991" stroke-width="1.6"/></svg></div>
  </header>
  <nav class="main-nav">
    <span class="active">HOME</span><span>ABOUT US</span><span>EVENTS</span><span>SERVE</span><span>BLOG</span><span>GIVE</span><span>CONNECT</span><span>CONTACT</span>
  </nav>
  <section class="hero">
    <div class="photo" role="img" aria-label="Crowd marching down a street holding a blue and yellow banner for the town" style="position:absolute;inset:0"></div>
    <div class="dots"><i class="on"></i><i></i><i></i><i></i></div>
  </section>

  <section class="features">
    <div class="cards4">
      <div class="feature"><div class="top"><svg width="16" height="16" viewBox="0 0 16 16"><rect x="3" y="1" width="10" height="14" fill="none" stroke="#fff" stroke-width="1.5"/><line x1="5" y1="5" x2="11" y2="5" stroke="#fff"/><line x1="5" y1="8" x2="11" y2="8" stroke="#fff"/></svg>IMPACT</div><div class="photo" role="img" aria-label="Volunteers gathered outdoors"></div></div>
      <div class="feature"><div class="top"><svg width="16" height="16" viewBox="0 0 16 16"><path d="M1 6 8 1l7 5z" fill="#fff"/><rect x="3" y="7" width="2" height="6" fill="#fff"/><rect x="7" y="7" width="2" height="6" fill="#fff"/><rect x="11" y="7" width="2" height="6" fill="#fff"/><rect x="1" y="13" width="14" height="2" fill="#fff"/></svg>COMMUNITY</div><div class="photo" role="img" aria-label="People holding hand-made signs"></div></div>
      <div class="feature"><div class="top"><svg width="16" height="16" viewBox="0 0 16 16"><path d="M8 14s-6-4-6-8a3 3 0 0 1 6-1 3 3 0 0 1 6 1c0 4-6 8-6 8z" fill="#fff"/></svg>ENTHUSIASM</div><div class="photo" role="img" aria-label="Smiling neighbour at a town event"></div></div>
      <div class="feature red"><div class="top"><svg width="16" height="16" viewBox="0 0 16 16"><polyline points="2,8 6,12 14,3" fill="none" stroke="#fff" stroke-width="2"/></svg>SERVING</div><div class="photo" role="img" aria-label="Crowd with red and white flags" style="background:linear-gradient(135deg,#d46a74,#7d3340)"></div></div>
    </div>
    <div class="activism">
      <h2>Activism<small>Love your town, serve your town</small></h2>
      <p>We are a group of neighbours who believe our town is worth loving. Join serve projects, social nights and simple acts of kindness that make Ashbury a better home for all of us.</p>
      <span class="btn"><span class="sq"></span>BECOME A MEMBER</span>
    </div>
  </section>

  <section class="rights">
    <h2 class="section-title">Get up for your town</h2>
    <div class="collage">
      <div class="photo c1" role="img" aria-label="Marchers holding red placards"></div>
      <div class="photo big" role="img" aria-label="Speaker on stage addressing a large audience"></div>
      <div class="photo c3" role="img" aria-label="Volunteer holding a megaphone"></div>
      <div class="photo c2" role="img" aria-label="Hands raised at an outdoor gathering"></div>
      <div class="photo c4" role="img" aria-label="Supporters waving flags at a rally"></div>
    </div>
  </section>

  <section class="events">
    <h2 class="section-title">Upcoming events</h2>
    <div class="events-grid">
      <article class="event"><div class="photo" role="img" aria-label="Neighbours at a street cleanup" style="background:linear-gradient(135deg,#b84a58,#6d8da0)"></div><h3>Park Cleanup</h3><div class="date">Saturday, 9:00 am — Centennial Park</div><p>Gloves, bags and coffee provided. Bring a friend and help care for our parks.</p><div class="more">See event details</div></article>
      <article class="event"><div class="photo" role="img" aria-label="Person with raised arm against the sky" style="background:linear-gradient(180deg,#a8c3d6,#4f6f7e)"></div><h3>Food Drive Night</h3><div class="date">Thursday, 6:30 pm — Main Street Hall</div><p>Sort and pack groceries for families across Ashbury and nearby towns.</p><div class="more">See event details</div></article>
      <article class="event"><div class="photo" role="img" aria-label="Friends laughing at an outdoor picnic" style="background:linear-gradient(135deg,#d47a5a,#4a6a80)"></div><h3>Neighbour Picnic</h3><div class="date">Sunday, 12:00 pm — Lakeside Green</div><p>Food, games and music for the whole family. Everyone is welcome here.</p><div class="more">See event details</div></article>
    </div>
  </section>

  <section class="donation">
    <h2 class="section-title">Make donation</h2>
    <div class="donation-row">
      <div class="donate-form"><div class="field">Full name</div><div class="field">Email address</div><div class="field">Amount</div></div>
      <div class="donation-text">
        <p>Every gift goes straight to serve projects, supplies and events that bless our town. Give once or set up a monthly gift in a few quick steps.</p>
        <p style="margin-top:8px">Thank you for standing with your neighbours and for helping us show that we are for Ashbury.</p>
        <span class="btn-light">DONATE</span>
      </div>
    </div>
  </section>

  <section class="voices">
    <h2 class="section-title">Voice of people</h2>
    <div class="voices-panel">
      <div class="quote"><div class="photo" role="img" aria-label="Portrait of a volunteer" style="background:linear-gradient(135deg,#c9b8a8,#7a6a66)"></div><div><p>Serving with this group showed me how much good is already in our town. I met neighbours I had passed for years.</p><strong>Dana Miller</strong><span>Volunteer</span></div></div>
      <div class="quote"><div class="photo" role="img" aria-label="Portrait of a community member" style="background:linear-gradient(135deg,#b65a64,#4e5e6a)"></div><div><p>The picnic nights are the best part of my month. My kids look forward to them and so do I, every time.</p><strong>Greg Holt</strong><span>Parent</span></div></div>
      <div class="quote"><div class="photo" role="img" aria-label="Portrait of a young volunteer" style="background:linear-gradient(135deg,#a9bdc9,#567080)"></div><div><p>I came for one cleanup day and stayed for the people. It feels good to be part of something for our home.</p><strong>Amy Ruiz</strong><span>Student</span></div></div>
      <div class="quote"><div class="photo" role="img" aria-label="Portrait of a local business owner" style="background:linear-gradient(135deg,#d39a8a,#7a4a52)"></div><div><p>They show up when it counts. Our shop has seen real care from this crew during a hard season.</p><strong>Leo Grant</strong><span>Shop owner</span></div></div>
    </div>
  </section>

  <section class="shop">
    <h2 class="section-title">Buy for help</h2>
    <div class="products">
      <div class="product"><div class="photo" role="img" aria-label="White t-shirt with a printed town slogan"></div><h3>KIND TOWN T-SHIRT</h3><div class="cat">Apparel</div><div class="price">$19.00</div><div class="actions"><span>Add to cart</span><span>Details</span></div></div>
      <div class="product"><div class="photo" role="img" aria-label="Printed poster with figures"></div><h3>SERVE POSTER</h3><div class="cat">Print</div><div class="price">$9.00</div><div class="actions"><span>Add to cart</span><span>Details</span></div></div>
      <div class="product"><div class="photo" role="img" aria-label="Grey t-shirt with a printed graphic"></div><h3>NEIGHBOUR TEE</h3><div class="cat">Apparel</div><div class="price">$19.00</div><div class="actions"><span>Add to cart</span><span>Details</span></div></div>
      <div class="product"><div class="photo" role="img" aria-label="White poster with a red graphic"></div><h3>TOWN POSTER</h3><div class="cat">Print</div><div class="price">$9.00</div><div class="actions"><span>Add to cart</span><span>Details</span></div></div>
    </div>
  </section>

  <section class="members">
    <h2 class="section-title">Our members</h2>
    <div class="members-grid">
      <div class="member"><div class="photo" role="img" aria-label="Member in colourful outfit at a parade" style="background:linear-gradient(135deg,#e0b14a,#6a4a8a)"></div><h3>Lena Park</h3><div class="role">Events lead</div><div class="socials"><i></i><i></i><i></i><i></i></div></div>
      <div class="member"><div class="photo" role="img" aria-label="Member cheering with friends" style="background:linear-gradient(135deg,#8aaec4,#3f5b6a)"></div><h3>Marcus Reed</h3><div class="role">Serve coordinator</div><div class="socials"><i></i><i></i><i></i><i></i></div></div>
      <div class="member"><div class="photo" role="img" aria-label="Member in costume at a street festival" style="background:linear-gradient(135deg,#d0505c,#3a4e5a)"></div><h3>Tessa Lowe</h3><div class="role">Outreach</div><div class="socials"><i></i><i></i><i></i><i></i></div></div>
    </div>
  </section>

  <section class="progress">
    <h2 class="section-title">Our progress</h2>
    <div class="progress-grid">
      <div class="stat"><svg width="30" height="30" viewBox="0 0 30 30"><circle cx="15" cy="10" r="6" fill="none" stroke="#d3dee6" stroke-width="2"/><path d="M4 28c1-7 6-10 11-10s10 3 11 10" fill="none" stroke="#d3dee6" stroke-width="2"/></svg><div><b>0</b><span class="lbl">Volunteers</span></div></div>
      <div class="stat"><svg width="30" height="30" viewBox="0 0 30 30"><path d="M15 26s-11-7-11-14a6 6 0 0 1 11-3 6 6 0 0 1 11 3c0 7-11 14-11 14z" fill="none" stroke="#d3dee6" stroke-width="2"/></svg><div><b>0</b><span class="lbl">Projects</span></div></div>
      <div class="stat"><svg width="30" height="30" viewBox="0 0 30 30"><polygon points="15,3 18.5,11 27,11.5 20.5,17 22.5,26 15,21 7.5,26 9.5,17 3,11.5 11.5,11" fill="none" stroke="#d3dee6" stroke-width="2"/></svg><div><b>0</b><span class="lbl">Events held</span></div></div>
      <div class="stat"><svg width="30" height="30" viewBox="0 0 30 30"><line x1="6" y1="3" x2="6" y2="28" stroke="#d3dee6" stroke-width="2"/><path d="M6 5h18l-4 6 4 6H6" fill="none" stroke="#d3dee6" stroke-width="2"/></svg><div><b>$0</b><span class="lbl">Funds raised</span></div></div>
    </div>
  </section>

  <section class="news">
    <h2 class="section-title">Latest news</h2>
    <div class="news-grid">
      <article class="post"><div class="photo" role="img" aria-label="Flag waving over a crowd" style="background:linear-gradient(135deg,#c4485a,#e8e8ee 60%,#3e6a7a)"></div><h3>Cleanup Recap</h3><div class="meta">May 12 · 3 comments</div></article>
      <article class="post"><div class="photo" role="img" aria-label="Families at a town fair" style="background:linear-gradient(135deg,#c9a06a,#5a6e7a)"></div><h3>Summer Serve Days</h3><div class="meta">May 8 · 5 comments</div></article>
      <article class="post"><div class="photo" role="img" aria-label="Hand-made red heart sign" style="background:linear-gradient(135deg,#f0f0f4,#c4485a)"></div><h3>Why We Love Ashbury</h3><div class="meta">May 2 · 2 comments</div></article>
      <article class="post"><div class="photo" role="img" aria-label="Dancer at an outdoor celebration" style="background:linear-gradient(135deg,#e4e6ec,#7a8c98)"></div><h3>Block Party Photos</h3><div class="meta">Apr 27 · 4 comments</div></article>
    </div>
  </section>

  <section class="twitter">
    <div class="flag" role="img" aria-label="Faint waving flag in the background"></div>
    <div class="tw-mark"></div>
    <div class="handle">@kindashbury</div>
    <p>Thanks to everyone who showed up for Saturday's park cleanup — forty bags of trash and a lot of new friends. #kindashbury</p>
    <div class="dots"><i class="on"></i><i></i><i></i></div>
  </section>

  <section class="funds">
    <h2 class="section-title">Collected funds</h2>
    <div class="funds-grid">
      <div class="fund"><div class="lbl">Food Drive</div><b>0%</b></div>
      <div class="fund"><div class="lbl">Park Renewal</div><b>0%</b></div>
      <div class="fund"><div class="lbl">Youth Nights</div><b>0%</b></div>
      <div class="fund"><div class="lbl">Winter Coats</div><b>0%</b></div>
    </div>
  </section>

  <footer class="footer">
    <div class="footer-row">
      <div class="footer-brand">Harbor Light<br>Church</div>
      <div class="social-activity"><i></i>Social Activity</div>
    </div>
    <div class="circles"><i></i><i></i></div>
    <div class="rule"></div>
    <div class="legal">© KindAshbury.com — for our town</div>
  </footer>
</div>
</body>
</html>
```